Boutique furnished offices with "high end" childcare centre require Wordpress website template

Project Overview: We require a wordpress design for a new company based in South Perth Western Australia, "The Harbour 19 Collective" which provide centres where parents can utilise childcare whilst hiring furnished offices and co-working spaces. We also provide onsite beauty, hair, gymnasium and park & ride facilities into the CBD which can all be booked online through our website (plugins required to be used to book through https://quickslotter.example/). We are a one stop shop where you can drop your children at childcare, skip the traffic and ride the ferry into the CBD. Or simply have your children cared for whilst you work out of our furnished office facilities.
The website design should be classy, modern, gender neutral and corporate (not too children focused/playful).

Look And Feel: clean, classy, modern site which is easy to navigate and book services online. It must also be gender neutral and corporate (not children focused/playful).
A typical childcare centre feel - we aren’t going for "jellybeans and teddybears" we are looking for a classy, corporate and sophisticated feel.

(LOGO currently being finalised but is charcoal grey on a white back ground and attached below - but will all be in lower case not capitals)

Target Market(s)

Target market is working parents, predominantly corporate or consultants running their own businesses.

Industry/Entity Type

Boutique

Number of Pages Required

2 page

Requirements
Must have
• The following would be required of the winning submission:
• • Clean, classy, modern site which is easy to navigate and book services online. It must also be gender neutral and corporate (not children focused/playful).
• • Require simplistic homepage with Menu of list of services, and template for individual pages for each of the services offered (child care, furnished offices, park & ride, hair/ beauty, gymnasium)
• • Necessary customization/plugins to allow online bookings to be placed https://quickslotter.example/
• • Well placed plugin/customization to link and also allow "share it" type links to major social networks (linkedin, facebook, twitter, google+, etc.).
• • All design components should be optimized for indexing on major search engines
• • Wordpress theme that is supported in Chrome, IE 8+, firefox, and safari
Nice to have
• Included below is a list of sites that we like from a simplicity and clean look and feel.
• http://www.lumenfold.example.au/
• http://www.wanderthegardenpath.example.uk/
• http://www.velopiccolo.example/
• http://www.qvframe.example.au/
• http://madebymarten.example/

```html
<!DOCTYPE html>
<html lang="en">
<head>
<meta charset="utf-8">
<title>The Harbour 19 Collective</title>
<link rel="stylesheet" href="https://fonts.googleapis.com/css2?family=Jost:wght@400;500&family=Open+Sans:wght@400;600&display=swap">
<style>
:root{
  --brand:#29a8d6;
  --ink:#2b2b2b;
  --text:#555;
  --muted:#8a8a8a;
  --line:#d9d9d9;
  --footer:#f4f4f4;
  --white:#fff;
  --logo:#5a5a5a;
  --partner:#a3a6ab;
}
*{box-sizing:border-box;margin:0;padding:0}
html,body{width:1200px;height:2381px;overflow:hidden}
body{position:relative;background:var(--white);font-family:"Open Sans",Arial,sans-serif;color:var(--text)}
h1,h2,h3,h4{font-weight:400}

/* header */
.site-header{position:absolute;left:0;top:0;width:1200px;height:114px;background:var(--white)}
.brand{position:absolute;left:92px;top:44px;font-family:"Jost",Arial,sans-serif;font-weight:500;font-size:17px;letter-spacing:1px;color:var(--logo);line-height:32px;white-space:nowrap}
.brand--footer{left:92px;top:2204px;font-size:13px;letter-spacing:.6px;line-height:24px}
.main-nav{position:absolute;top:42px;left:456px;display:flex;align-items:center;font-family:"Jost",Arial,sans-serif;font-size:15px;color:var(--ink);letter-spacing:.3px}
.main-nav a{color:inherit;text-decoration:none;margin-right:54px;line-height:34px}
.main-nav a:last-child{margin-right:0}
.main-nav .is-active{color:var(--brand);border:1.5px solid var(--brand);border-radius:18px;padding:0 14px;display:flex;align-items:center;gap:5px;margin-right:42px}

/* hero */
.hero-media{position:absolute;left:0;top:114px;width:1200px;height:589px;
  background:radial-gradient(ellipse at 70% 45%,#f2e2cf 0,#d9b891 28%,transparent 55%),
  linear-gradient(90deg,#6b3a10 0%,#b8741c 22%,#8a5418 45%,#caa277 70%,#e9dccd 100%)}
.hero-title{position:absolute;left:90px;top:350px;font-family:"Jost",Arial,sans-serif;font-weight:500;font-size:39px;color:var(--white);letter-spacing:.5px;white-space:nowrap}
.hero-sub{position:absolute;left:90px;top:400px;width:470px;font-size:24px;line-height:33px;color:var(--white)}
.hero-btn{position:absolute;left:92px;top:484px;width:140px;height:40px;border:1.5px solid var(--white);border-radius:20px;color:var(--white);font-size:16px;display:flex;align-items:center;justify-content:center;gap:4px}
.slider-dots{position:absolute;left:93px;top:660px;display:flex;gap:4px}
.slider-dots span{width:10px;height:10px;border-radius:50%;background:var(--white)}
.slider-dots span.is-current{background:var(--brand)}

/* section titles */
.section-title{position:absolute;left:0;width:1200px;text-align:center;font-family:"Jost",Arial,sans-serif;font-weight:400;font-size:29px;letter-spacing:.5px;color:var(--brand)}

/* services */
.service{position:absolute;width:470px;height:112px}
.service-photo{position:absolute;left:0;top:0;width:111px;height:111px;border-radius:50%;border:3px solid #e6e6e6}
.service-name{position:absolute;left:125px;top:10px;font-family:"Jost",Arial,sans-serif;font-weight:400;font-size:17px;color:var(--ink);letter-spacing:.3px}
.service-text{position:absolute;left:125px;top:40px;width:345px;font-size:12.5px;line-height:19px;color:var(--muted)}

/* booking */
.booking{position:absolute;left:0;top:1155px;width:1200px;height:375px;background:linear-gradient(180deg,#31addb,#27a6d4)}
.booking .section-title{color:var(--white);top:52px}
.booking-lead{position:absolute;top:104px;left:0;width:1200px;text-align:center;font-size:13px;color:var(--white)}
.field{position:absolute;width:320px;height:48px;background:var(--white);border-radius:3px;font-size:14px;color:#555;padding-left:18px;display:flex;align-items:center;box-shadow:0 1px 2px rgba(0,0,0,.08)}
.field svg{position:absolute;right:18px;top:18px}
.start-btn{position:absolute;left:513px;top:294px;width:174px;height:48px;border-radius:24px;background:linear-gradient(180deg,#fafafa,#dcdcdc);box-shadow:0 2px 4px rgba(0,0,0,.2);font-family:"Jost",Arial,sans-serif;font-size:18px;color:var(--ink);display:flex;align-items:center;justify-content:center}

/* blog */
.post{position:absolute;top:1662px;width:311px}
.post-photo{width:311px;height:198px}
.post-title{margin-top:22px;text-align:center;font-family:"Jost",Arial,sans-serif;font-weight:400;font-size:16px;color:var(--ink)}
.post-date{margin-top:3px;text-align:center;font-size:11.5px;color:var(--text)}

/* partners */
.partners{position:absolute;left:110px;top:2000px;width:980px;display:flex;justify-content:space-between;align-items:center;height:42px}
.partner{font-family:"Jost",Arial,sans-serif;font-weight:500;font-size:30px;color:var(--partner)}

/* footer */
.site-footer{position:absolute;left:0;top:2084px;width:1200px;height:297px;background:var(--footer)}
.footer-heading{position:absolute;top:2142px;font-family:"Jost",Arial,sans-serif;font-weight:400;font-size:15px;color:var(--ink);letter-spacing:.3px}
.footer-text{position:absolute;font-size:12px;line-height:21px;color:#777}
.newsletter{position:absolute;left:605px;top:2220px;display:flex}
.newsletter-input{width:148px;height:31px;background:var(--white);border:1px solid var(--line);font-size:11.5px;color:#777;padding-left:8px;display:flex;align-items:center}
.newsletter-btn{width:58px;height:31px;background:var(--brand);color:var(--white);font-size:12px;display:flex;align-items:center;justify-content:center}
.social{position:absolute;left:938px;top:2186px;display:flex;gap:14px}
.social span{width:24px;height:24px;border-radius:4px;background:#6a6a6a}
.footer-rule{position:absolute;left:92px;top:2309px;width:1022px;height:1px;background:#cfcfcf}
.copyright{position:absolute;top:2336px;left:0;width:1200px;text-align:center;font-size:12px;color:var(--ink)}
</style>
</head>
<body>

<header class="site-header">
  <div class="brand">HARBOUR 19 COLLECTIVE</div>
  <nav class="main-nav">
    <a class="is-active" href="#">
      <svg width="13" height="12" viewBox="0 0 13 12"><path d="M6.5 0 0 5.5h2V12h3.2V8h2.6v4H11V5.5h2z" fill="currentColor"/></svg>HOME</a>
    <a href="#">ABOUT US</a>
    <a href="#">SERVICES</a>
    <a href="#">SUPPORTS</a>
    <a href="#">BLOG</a>
    <a href="#">CONTACTS</a>
  </nav>
</header>

<section class="hero">
  <div class="hero-media" role="img" aria-label="Smiling mother hugging her young daughter at a warmly lit fairground carousel"></div>
  <h1 class="hero-title">THE HARBOUR 19 COLLECTIVE</h1>
  <p class="hero-sub">Neque porro quisquam est qui ipsum quia dolor sit amet consectetur</p>
  <div class="hero-btn">View More
    <svg width="10" height="10" viewBox="0 0 10 10"><path d="M1 1l4 4-4 4M5 1l4 4-4 4" stroke="#fff" stroke-width="1.6" fill="none"/></svg></div>
  <div class="slider-dots"><span class="is-current"></span><span></span><span></span><span></span><span></span></div>
</section>

<h2 class="section-title" style="top:752px">OUR SERVICES</h2>

<article class="service" style="left:92px;top:836px">
  <div class="service-photo" role="img" aria-label="Mother and daughter drawing together at a table" style="background:linear-gradient(135deg,#c98b6a,#e9cfc0 55%,#7fa6c9)"></div>
  <h3 class="service-name">CHILD CARE</h3>
  <p class="service-text">Lorem Ipsum has been the industry's standard dummy text ever since the 1500s, when an unknown printer took a galley of type and scrambled it to make a specimen book</p>
</article>
<article class="service" style="left:641px;top:842px">
  <div class="service-photo" role="img" aria-label="Children riding a colourful fairground ride" style="background:linear-gradient(135deg,#9ab4d6,#d9c9a5 50%,#a85fa3)"></div>
  <h3 class="service-name">PARK &amp; RIDE</h3>
  <p class="service-text">Lorem Ipsum has been the industry's standard dummy text ever since the 1500s, when an unknown printer took a galley of type and scrambled it to make a specimen book</p>
</article>
<article class="service" style="left:92px;top:984px">
  <div class="service-photo" role="img" aria-label="Modern furnished office with desks and computers" style="background:linear-gradient(135deg,#44505e,#c9ced6 55%,#8c96a3)"></div>
  <h3 class="service-name">FURNISHED OFFICES</h3>
  <p class="service-text">Lorem Ipsum has been the industry's standard dummy text ever since the 1500s, when an unknown printer took a galley of type and scrambled it to make a specimen book</p>
</article>
<article class="service" style="left:641px;top:990px">
  <div class="service-photo" role="img" aria-label="Woman resting after a gym workout" style="background:linear-gradient(135deg,#6b5448,#b89a86 50%,#d8d2cc)"></div>
  <h3 class="service-name">GYMNASIUM</h3>
  <p class="service-text">Lorem Ipsum has been the industry's standard dummy text ever since the 1500s, when an unknown printer took a galley of type and scrambled it to make a specimen book</p>
</article>

<section class="booking">
  <h2 class="section-title">ONLINE BOOKING</h2>
  <p class="booking-lead">Lorem Ipsum has been the industry's standard dummy text ever since the 1500s, when an unknown printer took</p>
  <div class="field" style="left:110px;top:151px">Company login</div>
  <div class="field" style="left:451px;top:151px">Email</div>
  <div class="field" style="left:793px;top:151px">Phone</div>
  <div class="field" style="left:110px;top:219px">Business category
    <svg width="12" height="8" viewBox="0 0 12 8"><path d="M1 1l5 5 5-5" stroke="#444" stroke-width="1.6" fill="none"/></svg></div>
  <div class="field" style="left:451px;top:219px">Address</div>
  <div class="field" style="left:793px;top:219px">Company name</div>
  <div class="start-btn">START NOW</div>
</section>

<h2 class="section-title" style="top:1598px">OUR BLOG</h2>

<article class="post" style="left:94px">
  <div class="post-photo" role="img" aria-label="Bright office reception desk with an orange feature wall" style="background:linear-gradient(135deg,#b9563a 0,#d8cfc4 45%,#8e8e8e 100%)"></div>
  <h3 class="post-title">Neque porro quisquam est qui</h3>
  <p class="post-date">19/11/16</p>
</article>
<article class="post" style="left:446px">
  <div class="post-photo" role="img" aria-label="Mother and child riding a bumper car at a fair" style="background:linear-gradient(135deg,#4f8f6b,#c9b597 45%,#8a6b4d)"></div>
  <h3 class="post-title">Dolorem ipsum quia dolor sit amet</h3>
  <p class="post-date">17/11/16</p>
</article>
<article class="post" style="left:795px">
  <div class="post-photo" role="img" aria-label="Group fitness class exercising in a gym" style="background:linear-gradient(135deg,#e9e4dc,#5b7fa8 50%,#d7b07a)"></div>
  <h3 class="post-title">Quisquam est qui dolorem</h3>
  <p class="post-date">13/11/16</p>
</article>

<div class="partners">
  <span class="partner">RAVEL</span>
  <span class="partner">Ostrin</span>
  <span class="partner">DELVANE</span>
  <span class="partner">Quorra</span>
  <span class="partner">grenlo</span>
  <span class="partner">FENNIC</span>
</div>

<footer class="site-footer"></footer>
<div class="brand brand--footer">HARBOUR 19 COLLECTIVE</div>

<h4 class="footer-heading" style="left:324px">CONTACT US</h4>
<p class="footer-text" style="left:324px;top:2178px">Address : 12 Larkspur Lane, Old Quay<br>Eastmoor, EQ4 7LN<br>Phone : 555-018-2740.<br>Email : info@harbour19.example</p>

<h4 class="footer-heading" style="left:605px">JOIN OUR MAILING LIST</h4>
<p class="footer-text" style="left:605px;top:2178px;width:210px;font-size:11.5px;line-height:18px">Your about us information would fit here nicely.</p>
<div class="newsletter">
  <div class="newsletter-input">Email address</div>
  <div class="newsletter-btn">Submit</div>
</div>

<h4 class="footer-heading" style="left:938px">FOLLOW US OUT THERE</h4>
<div class="social" aria-label="Social links"><span></span><span></span><span></span><span></span></div>

<div class="footer-rule"></div>
<p class="copyright">Copyright © 2016. All Rights Reserved</p>

</body>
</html>
```